Business Cards for Communications Technology Company

We are an innovative software company based in Tropical North Queensland, Australia. We have several brands with a focus on communications software for businesses. We are looking for a business card that is very innovate and creative whilst still remaining professional on a corporate level.

Our internal culture is very progressive and expresses a blend between the clarity of our natural surroundings and the highly technological industry we work in. Our current branding blends a modern minimalist typeface with the desire to push the boundaries in the way we communicate.

This is a corporate level business card for the communications software industry and may possibly also encompass our brands MarNetwork, PelFax, TukMailer and our B2B marketing service—with our companies name being Viresca Partners. Showing other brands on the business card is optional not compulsory.

Technical notes:

-We will attach all logo's and some examples of our corporate branding
- Would be willing to print with various papers, embossed, metallic ink, curved edges etc. in a standard business card size

Sample content:

Rowan Pellick
Senior Account Manager
Phone: 1300 842 916 / +617 4583 2764
Email: r.pellick@viresca.com.au
Web: www.viresca.com.au

Sincerely,
Viresca Partners.

```html
<!DOCTYPE html>
<html lang="en">
<head>
<meta charset="utf-8">
<title>Viresca Partners — Business Card</title>
<link rel="stylesheet" href="https://fonts.googleapis.com/css2?family=Open+Sans:wght@400;600;700&display=swap">
<style>
  :root {
    --backdrop: #2e2e2e;
    --card: #141414;
    --card-edge: #1e1e1e;
    --accent: #7dc242;
    --text-light: #e6e6e6;
    --text-muted: #a9a9a9;
    --divider: #262626;
    --silver: #b8b8b8;
  }
  * { box-sizing: border-box; margin: 0; padding: 0; }
  html, body {
    width: 1200px; height: 900px; overflow: hidden;
    background: var(--backdrop);
    font-family: "Open Sans", Arial, sans-serif;
  }
  .stage {
    width: 1200px; height: 900px;
    display: flex; align-items: center; justify-content: center; gap: 60px;
  }
  .card {
    width: 500px; height: 290px;
    background: var(--card);
    border: 1px solid var(--card-edge);
    border-radius: 18px;
    position: relative;
    box-shadow: 0 10px 30px rgba(0,0,0,.45);
  }
  /* Front card */
  .card-front { display: flex; }
  .brand-panel {
    width: 210px; height: 100%;
    display: flex; flex-direction: column; align-items: center; justify-content: center; gap: 14px;
    border-right: 1px solid var(--divider);
  }
  .brand-dot {
    width: 70px; height: 70px; border-radius: 50%;
    background: var(--accent);
  }
  .brand-name {
    color: var(--silver); font-weight: 600; font-size: 17px; letter-spacing: .5px;
  }
  .details {
    padding: 64px 0 0 30px;
  }
  .person-name {
    color: var(--accent); font-weight: 700; font-size: 21px; line-height: 1.1;
  }
  .person-role {
    color: var(--text-light); font-size: 12.5px; margin-top: 3px;
  }
  .contact-list { list-style: none; margin-top: 26px; }
  .contact-list li {
    display: flex; align-items: center; gap: 10px;
    color: var(--text-light); font-size: 13px; line-height: 22px;
  }
  .contact-list svg { width: 11px; height: 11px; fill: var(--accent); flex: none; }
  /* Back card */
  .card-back {
    display: flex; align-items: center; justify-content: center; gap: 14px;
  }
  .back-dot {
    width: 34px; height: 34px; border-radius: 50%; background: var(--accent);
  }
  .back-name {
    color: var(--silver); font-weight: 600; font-size: 34px; letter-spacing: 1px;
  }
</style>
</head>
<body>
<main class="stage">
  <section class="card card-front" aria-label="Business card front">
    <div class="brand-panel">
      <span class="brand-dot"></span>
      <span class="brand-name">Viresca Partners</span>
    </div>
    <div class="details">
      <h1 class="person-name">Rowan Pellick</h1>
      <p class="person-role">Senior Account Manager</p>
      <ul class="contact-list">
        <li>
          <svg viewBox="0 0 12 12" aria-hidden="true"><path d="M2.4 0.6 4.3 2.5 3.3 4.1c.7 1.6 1.9 2.9 3.5 3.6l1.5-1 1.9 1.9-1.2 1.8C5 10 1.9 6.9 0.6 1.8z"/></svg>
          1300 842 916 / +617 4583 2764
        </li>
        <li>
          <svg viewBox="0 0 12 12" aria-hidden="true"><path d="M0 2h12v8H0z M1 3l5 3.5L11 3v-.2H1z" fill-rule="evenodd"/></svg>
          r.pellick@viresca.com.au
        </li>
        <li>
          <svg viewBox="0 0 12 12" aria-hidden="true"><circle cx="6" cy="6" r="6"/><path d="M0 6h12M6 0v12" stroke="#141414" stroke-width="1"/></svg>
          www.viresca.com.au
        </li>
      </ul>
    </div>
  </section>

  <section class="card card-back" aria-label="Business card back">
    <span class="back-dot"></span>
    <span class="back-name">Viresca Partners</span>
  </section>
</main>
</body>
</html>
```